Recycling and Rubbish services for Residential and Commercial customers

We are after a complete redesign or freshening up of our current website.
www.trevlok.co.nz
On this site the general public can rent or buy rollaTUBs or skips for rubbish and recycling collection around the Nelson and Tasman area of New Zealand.

Target Market(s)

18 to 100 year old males and females in Nelson and Tasman area of New Zealand

Industry/Entity Type

Waste Management

Contact Information for Business Card

logo name title email phone web site address all the normal stuff

Number of Pages Required

5+ page

Colors

Designer to choose colors to be used in the design.

Requirements
Must have
• Has to be very fast and easy for the customer to rent bin, skip, tags, liner etc..
• see web site www.trevlok.co.nz
• An address finder so we can show two rates for urban and rural streets
Nice to have
• "We’re trying to get back to a more human face. Our customers appreciate that we are locals too. We are proud to be able to support our local community through sponsorship and donations."

```html
<!DOCTYPE html>
<html lang="en">
<head>
<meta charset="utf-8">
<title>Trevlok – Recycling and Rubbish Services</title>
<link rel="stylesheet" href="https://fonts.googleapis.com/css2?family=Roboto+Condensed:wght@400;700&family=Open+Sans:wght@400;600;700&display=swap">
<style>
:root{
  --green:#3f8a2c;
  --green-dark:#2c6a1e;
  --green-deep:#1f5116;
  --red:#d8202a;
  --white:#ffffff;
  --ink:#222222;
  --grey-band:#e4e4e4;
  --grey-line:#d0d0d0;
  --photo-sky:#b9c9cf;
  --photo-truck:#6f8e55;
}
*{box-sizing:border-box;margin:0;padding:0}
html,body{width:1200px;height:2440px;overflow:hidden;background:var(--white)}
body{position:relative;font-family:"Open Sans",Arial,sans-serif;color:var(--ink)}
.abs{position:absolute}

/* top utility bar */
.utility-bar{left:0;top:0;width:1200px;height:18px;background:var(--green-dark)}
.utility-links{right:76px;top:2px;display:flex;gap:20px;font-size:10px;font-weight:600;color:var(--white);letter-spacing:.5px}

/* header */
.site-header{left:0;top:18px;width:1200px;height:118px;background:var(--white)}
.brand{left:76px;top:12px;width:96px;height:96px;background:var(--green);display:flex;align-items:center;justify-content:center;color:var(--white);font-family:"Roboto Condensed",sans-serif;font-weight:700;font-size:22px;text-transform:uppercase}
.main-nav{left:234px;top:48px;display:flex;gap:26px;font-family:"Roboto Condensed",sans-serif;font-weight:700;font-size:19px}
.search-icon{left:1104px;top:44px}

/* hero */
.hero{left:0;top:136px;width:1200px;height:526px;background:var(--green)}
.hero-photo{left:340px;top:0;width:860px;height:526px;background:linear-gradient(180deg,var(--photo-sky) 0%,#9fb1a0 40%,var(--photo-truck) 75%,#707a70 100%);clip-path:polygon(14% 0,100% 0,100% 100%,0 100%)}
.hero-title{left:70px;top:182px;width:330px;color:var(--white);font-family:"Roboto Condensed",sans-serif;font-weight:700;font-size:34px;line-height:1.12;text-transform:uppercase}
.btn{display:inline-flex;align-items:center;justify-content:center;background:var(--red);color:var(--white);font-family:"Roboto Condensed",sans-serif;font-weight:700;font-size:15px;text-transform:uppercase;letter-spacing:.3px}
.hero-btn{left:70px;top:346px;width:130px;height:36px}

/* audience cards */
.audience-card{top:728px;width:516px;height:332px;overflow:hidden}
.audience-card .photo{position:absolute;inset:0}
.audience-card h2{position:absolute;left:22px;top:20px;color:var(--white);font-family:"Roboto Condensed",sans-serif;font-weight:700;font-size:40px;text-transform:uppercase}
.audience-card .btn{position:absolute;left:22px;bottom:26px;width:136px;height:38px}

/* info tiles */
.info-tile{top:1112px;height:280px;background:var(--green-deep);color:var(--white);padding:22px 24px}
.info-tile h3{font-family:"Roboto Condensed",sans-serif;font-weight:700;font-size:30px;line-height:1.1;text-transform:uppercase}
.btn-outline{position:absolute;left:24px;bottom:26px;height:36px;padding:0 16px;border:2px solid var(--white);color:var(--white);font-family:"Roboto Condensed",sans-serif;font-weight:700;font-size:15px;display:flex;align-items:center;text-transform:uppercase}
.field{position:absolute;left:24px;width:268px;height:42px;border:2px solid var(--white);background:transparent;color:var(--white);font-size:15px;display:flex;align-items:center;padding-left:12px}
.rate-choice{position:absolute;left:92px;top:222px;display:flex;gap:18px;font-size:14px;align-items:center}
.radio{display:inline-block;width:12px;height:12px;border:2px solid var(--white);border-radius:50%;margin-right:5px;vertical-align:-1px}
.radio.on{background:var(--white)}

/* section heading */
.section-title{left:0;width:1200px;text-align:center;font-family:"Roboto Condensed",sans-serif;font-weight:700;font-size:30px;text-transform:uppercase}
.rule{height:2px;background:var(--ink)}

/* products */
.product-card{top:1520px;width:248px;height:260px;border:1px solid var(--grey-line);background:var(--white)}
.product-card .photo{position:absolute;left:20px;top:16px;width:206px;height:170px}
.product-card .btn{position:absolute;left:18px;bottom:16px;width:210px;height:40px}

/* quick buy */
.quick-band{left:0;top:1848px;width:1200px;height:282px;background:var(--grey-band)}
.quick-item{top:1964px;width:150px;height:100px;background:var(--white);border:1px solid var(--grey-line)}
.quick-item .photo{position:absolute;left:40px;top:18px;width:70px;height:64px}

/* footer */
.site-footer{left:0;top:2130px;width:1200px;height:282px;background:var(--green);color:var(--white)}
.footer-brand{left:72px;top:40px;width:120px;height:120px;background:var(--green-deep);display:flex;align-items:center;justify-content:center;font-family:"Roboto Condensed",sans-serif;font-weight:700;font-size:28px;text-transform:uppercase}
.footer-col h4{font-weight:400;font-size:22px;margin-bottom:14px}
.footer-col p,.footer-col li{font-size:14px;line-height:1.55;list-style:none}
.contact-row{display:flex;gap:10px;margin-bottom:10px}
.newsletter-input{width:280px;height:38px;background:var(--white);color:#555;font-size:14px;display:flex;align-items:center;justify-content:space-between;padding:0 12px}
.social{display:flex;gap:10px;margin-top:10px}
.social span{width:30px;height:30px;border:2px solid var(--white);border-radius:50%}
.bottom-strip{left:0;top:2412px;width:1200px;height:28px;background:var(--green-deep);color:var(--white);font-size:12px;display:flex;align-items:center;justify-content:space-between;padding:0 72px}
</style>
</head>
<body>

<div class="abs utility-bar"></div>
<nav class="abs utility-links"><span>ABOUT US</span><span>TESTIMONIALS</span><span>FAQ</span><span>CONTACT US</span></nav>

<header class="abs site-header">
  <div class="abs brand">Trevlok</div>
  <nav class="abs main-nav"><span>FOR HOME</span><span>FOR BUSINESS</span></nav>
  <svg class="abs search-icon" width="24" height="24" viewBox="0 0 24 24" fill="none" stroke="#333" stroke-width="2.6"><circle cx="10" cy="10" r="7"/><line x1="15" y1="15" x2="22" y2="22"/></svg>
</header>

<section class="abs hero">
  <div class="abs hero-photo" role="img" aria-label="Green rubbish collection truck on a suburban street"></div>
  <h1 class="abs hero-title">Lorem ipsum dolor sit amet, consectetur adipiscing elit</h1>
  <a class="abs btn hero-btn">Learn more</a>
</section>

<article class="abs audience-card" style="left:72px">
  <div class="photo" role="img" aria-label="Resident carrying a blue recycling crate" style="background:linear-gradient(135deg,#8c7c6c,#c9c2b6 55%,#5e7fa8)"></div>
  <h2>For Residential</h2>
  <a class="btn">Get started</a>
</article>
<article class="abs audience-card" style="left:612px">
  <div class="photo" role="img" aria-label="Red skip bins at a commercial yard" style="background:linear-gradient(180deg,#7f8b8c,#8d4a3c 55%,#5a3a30)"></div>
  <h2>For Business</h2>
  <a class="btn">Learn more</a>
</article>

<section class="abs info-tile" style="left:72px;width:336px;background:var(--green)">
  <h3>Opportunities too good to waste</h3>
  <a class="btn-outline">Careers</a>
</section>
<section class="abs info-tile" style="left:432px;width:316px;background:var(--green)">
  <h3>Find a refuse transfer station</h3>
  <div class="field" style="top:92px">No.</div>
  <div class="field" style="top:138px">Your Street</div>
  <a class="btn-outline" style="left:24px;top:210px;bottom:auto;height:36px;padding:0 12px">Go</a>
  <div class="rate-choice"><span><i class="radio on"></i>Urban</span><span><i class="radio"></i>Rural</span></div>
</section>
<section class="abs info-tile" style="left:772px;width:356px">
  <h3>Who we are</h3>
  <a class="btn-outline">Learn more</a>
</section>

<div class="abs rule" style="left:72px;top:1468px;width:412px"></div>
<h2 class="abs section-title" style="top:1448px">Product range</h2>
<div class="abs rule" style="left:716px;top:1468px;width:412px"></div>

<article class="abs product-card" style="left:72px"><div class="photo" role="img" aria-label="Green wheeled rubbish bins" style="background:linear-gradient(180deg,#f4f4f4,#3d7a30 40%,#2b5a22)"></div><a class="btn">Get your bin here</a></article>
<article class="abs product-card" style="left:344px"><div class="photo" role="img" aria-label="Green skip bin" style="background:linear-gradient(180deg,#f4f4f4 30%,#3f8a5a 45%,#2d6a44)"></div><a class="btn">Get your skip here</a></article>
<article class="abs product-card" style="left:612px"><div class="photo" role="img" aria-label="Large commercial bin" style="background:linear-gradient(180deg,#f4f4f4 15%,#4f7a3a 30%,#3a5f2b)"></div><a class="btn">Get commercial bin</a></article>
<article class="abs product-card" style="left:880px"><div class="photo" role="img" aria-label="Bin tags, liners and supplies" style="background:linear-gradient(135deg,#f4f4f4,#3f8a2c 45%,#d8202a 75%,#f4f4f4)"></div><a class="btn">Get bin supplies</a></article>

<div class="abs quick-band"></div>
<div class="abs rule" style="left:272px;top:1918px;width:200px"></div>
<h2 class="abs section-title" style="top:1898px;font-size:26px">Quick buy supplies</h2>
<div class="abs rule" style="left:728px;top:1918px;width:200px"></div>

<div class="abs quick-item" style="left:176px"><div class="photo" role="img" aria-label="Small green bin" style="background:var(--green)"></div></div>
<div class="abs quick-item" style="left:346px"><div class="photo" role="img" aria-label="Bin liner roll" style="background:#2d6a44"></div></div>
<div class="abs quick-item" style="left:516px"><div class="photo" role="img" aria-label="Collection tag pack" style="background:#c6c6c6"></div></div>
<div class="abs quick-item" style="left:686px"><div class="photo" role="img" aria-label="Blue bin tag" style="background:#4f86c6"></div></div>
<div class="abs quick-item" style="left:856px"><div class="photo" role="img" aria-label="Red bin tag" style="background:var(--red)"></div></div>

<footer class="abs site-footer">
  <div class="abs footer-brand">Trevlok</div>
  <div class="abs footer-col" style="left:348px;top:34px">
    <h4>Contact Us</h4>
    <div class="contact-row"><svg width="16" height="18" viewBox="0 0 16 18" fill="#fff"><path d="M8 0a6 6 0 0 0-6 6c0 5 6 12 6 12s6-7 6-12a6 6 0 0 0-6-6zm0 8.5A2.5 2.5 0 1 1 8 3.5a2.5 2.5 0 0 1 0 5z"/></svg><p>Trevlok<br>14 Kowhai Lane, Nelson</p></div>
    <div class="contact-row"><svg width="16" height="16" viewBox="0 0 24 24" fill="#fff"><path d="M6.6 10.8a15 15 0 0 0 6.6 6.6l2.2-2.2a1 1 0 0 1 1-.25 11.4 11.4 0 0 0 3.6.57 1 1 0 0 1 1 1V20a1 1 0 0 1-1 1A17 17 0 0 1 3 4a1 1 0 0 1 1-1h3.5a1 1 0 0 1 1 1c0 1.25.2 2.45.57 3.57a1 1 0 0 1-.25 1z"/></svg><p>Call us<br><strong>0800 555 019</strong></p></div>
    <div class="contact-row"><svg width="16" height="14" viewBox="0 0 24 18" fill="none" stroke="#fff" stroke-width="2"><rect x="1" y="1" width="22" height="16"/><path d="M1 1l11 9 11-9"/></svg><p>Email us<br>info@trevlok.co.nz</p></div>
  </div>
  <div class="abs footer-col" style="left:588px;top:34px">
    <h4>Quick Links</h4>
    <div style="display:flex;gap:56px">
      <ul><li>Home</li><li>About Us</li><li>Services</li><li>Testimonials</li></ul>
      <ul><li>FAQ</li><li>Media</li><li>Links</li><li>Contact Us</li></ul>
    </div>
  </div>
  <div class="abs footer-col" style="left:848px;top:34px">
    <h4>Subscribe Our Newsletter</h4>
    <div class="newsletter-input"><span>E-mail</span><svg width="22" height="12" viewBox="0 0 22 12" fill="none" stroke="#d8202a" stroke-width="2"><path d="M0 6h20M15 1l5 5-5 5"/></svg></div>
    <h4 style="margin-top:20px;margin-bottom:0">Keep in Touch</h4>
    <div class="social"><span></span><span></span><span></span><span></span></div>
  </div>
</footer>

<div class="abs bottom-strip"><span>Proudly Nelson owned and operated!</span><span>Copyright © 2017, Trevlok. All rights reserved</span></div>

</body>
</html>
```